Quarrow financial services, is a financial company that provides consultancy, brokerage services, and funding.

we will be providing the clients with insights, knowledge and data with regards to the financial markets.

with the brokerage services we will try to find the suitable counterparts that provide them with the best investments that suits their needs and expected return.

Target Market(s)

financial institutions, Corporates, high-net worth individuals

Industry/Entity Type

Financial Service

Contact Information for Business Card

Font styles to use
Other font styles liked:
• applemyungjo

Colors
00a990
848484

Requirements
Must have
• the logo at the back
Nice to have
• Finesse
Should not have
• boldness

```html
<!DOCTYPE html>
<html lang="en">
<head>
<meta charset="utf-8">
<title>Quarrow Financial Services – Business Card</title>
<link rel="stylesheet" href="https://fonts.googleapis.com/css2?family=Cinzel:wght@400&family=Montserrat:wght@400;500&display=swap">
<style>
  :root {
    --backdrop: #d1d2d4;
    --card-white: #ffffff;
    --slate: #434d55;
    --leaf: #7a9a45;
    --leaf-soft: #d3dfc4;
    --text-light: #ffffff;
  }
  * { margin: 0; padding: 0; box-sizing: border-box; }
  html, body { width: 1200px; height: 927px; overflow: hidden; }
  body { background: var(--backdrop); position: relative; font-family: "Montserrat", sans-serif; }

  .card { position: absolute; top: 104px; width: 410px; height: 718px; }
  .card--front { left: 171px; background: var(--card-white); color: var(--slate); }
  .card--back { left: 618px; background: var(--slate); color: var(--text-light); }

  .centered { position: absolute; left: 0; width: 100%; text-align: center; }

  .brand-square { position: absolute; left: 177px; top: 100px; width: 56px; height: 56px; background: var(--leaf-soft); }

  .brand-name, .brand-sub, .brand-line { font-family: "Cinzel", serif; font-weight: 400; line-height: 1; }

  .card--front .brand-name { top: 198px; font-size: 44px; letter-spacing: 2px; }
  .card--front .brand-sub { top: 244px; font-size: 13px; letter-spacing: 3.5px; }
  .card--front .brand-line { top: 265px; font-size: 10px; letter-spacing: 2px; }

  .card--back .brand-name { top: 300px; font-size: 60px; letter-spacing: 3px; }
  .card--back .brand-sub { top: 362px; font-size: 17px; letter-spacing: 4.5px; }
  .card--back .brand-line { top: 390px; font-size: 12px; letter-spacing: 2.5px; }

  .person-name { top: 440px; font-size: 26px; font-weight: 500; color: var(--leaf); letter-spacing: 0.5px; }
  .person-role { top: 473px; font-size: 18px; }
  .address { top: 500px; font-size: 18px; line-height: 22px; }
  .contact-icons { top: 556px; display: flex; justify-content: center; gap: 6px; }
  .contact-icons svg { width: 14px; height: 14px; stroke: var(--leaf); fill: none; stroke-width: 1.4; }
  .contact-list { top: 584px; font-size: 18.5px; line-height: 22.4px; }
  .web-accent { color: var(--leaf); font-weight: 500; }

  .card--back .website { top: 652px; font-size: 18px; letter-spacing: 0.5px; }
  .card--back .website strong { font-weight: 500; }
</style>
</head>
<body>
  <section class="card card--front">
    <div class="brand-square"></div>
    <div class="centered brand-name">QUARROW</div>
    <div class="centered brand-sub">FINANCIAL SERVICES</div>
    <div class="centered brand-line">CONSULTANCY · BROKERAGE · FUNDING</div>

    <div class="centered person-name">Marin Calloway</div>
    <div class="centered person-role">Director</div>
    <div class="centered address">P.O. Box 4180<br>Alder Falls, MI 49622</div>

    <div class="centered contact-icons">
      <svg viewBox="0 0 14 14" aria-label="phone"><path d="M3 1.5l2 .3.7 2.6-1.3 1a7 7 0 0 0 4.2 4.2l1-1.3 2.6.7.3 2a1.4 1.4 0 0 1-1.5 1.3A10.5 10.5 0 0 1 1.7 3 1.4 1.4 0 0 1 3 1.5z"/></svg>
      <svg viewBox="0 0 14 14" aria-label="mobile"><rect x="4" y="1" width="6.5" height="12" rx="1"/><line x1="6.5" y1="11" x2="8" y2="11"/></svg>
      <svg viewBox="0 0 14 14" aria-label="email"><rect x="1" y="3" width="12" height="8.5" rx="0.8"/><path d="M1.3 3.4L7 8l5.7-4.6"/></svg>
      <svg viewBox="0 0 14 14" aria-label="website"><circle cx="7" cy="7" r="5.8"/><ellipse cx="7" cy="7" rx="2.6" ry="5.8"/><line x1="1.2" y1="7" x2="12.8" y2="7"/><path d="M2.3 4h9.4M2.3 10h9.4"/></svg>
    </div>

    <div class="centered contact-list">
      (555) 014-2290<br>
      (555) 019-7731<br>
      info@quarrowfinancial.com<br>
      www.<span class="web-accent">quarrowfinancial</span>.com
    </div>
  </section>

  <section class="card card--back">
    <div class="centered brand-name">QUARROW</div>
    <div class="centered brand-sub">FINANCIAL SERVICES</div>
    <div class="centered brand-line">CONSULTANCY · BROKERAGE · FUNDING</div>
    <div class="centered website">www.<strong>quarrowfinancial</strong>.com</div>
  </section>
</body>
</html>
```